Flyerdesign DIN A4 Lang 6-seitig Wickelfalz für Seniorenhilfsverband
Flott - engagiert und entgegenkommend. Gerne wieder!
Zielgruppe
Die Dachorganisation betreibt mehrere Pflegeheime mit unterschiedlichen Themen (Demenz, körperliche Behinderung, etc...) sowie betreutes wohnen und ein Tageszentrum. Auch Verantaltungen und Seminare werden geboten.
Aufgabenstellung
GESUCHT ist ein FLYER-Design.
DIN A4 Lang 6-seitig Wickelfalz.
Es gibt bereits ein fertiges Webdesign, auf dessen Basis ein passendes Design für einen Wickelfalz-Flyer erstellt werden soll. Die Inhaltsdaten sowie ein BSP-Flyer sind im Download-ZIP. Was nun gebraucht wird ist ein ansprechendes Design ohne Inhalt für diesen Verband.

```html
<!DOCTYPE html>
<html lang="de">
<head>
<meta charset="utf-8">
<title>Haus Lindenhof – Wickelfalz-Flyer</title>
<link href="https://fonts.googleapis.com/css2?family=Libre+Baskerville:ital,wght@0,400;0,700;1,400&family=Open+Sans:ital,wght@0,400;0,600;0,700;1,400&display=swap" rel="stylesheet">
<style>
:root{
  --stage:#2b2b2b;
  --paper:#ffffff;
  --yellow:#f3c300;
  --yellow-soft:#fbe27a;
  --ink:#4a4a4a;
  --ink-soft:#7a7a7a;
  --rule:#d9d9d9;
  --photo-warm:#d9c3ae;
  --photo-cool:#c9d3d9;
  --photo-green:#9fb38a;
  --map:#e6e3d8;
}
*{box-sizing:border-box;margin:0;padding:0}
html,body{width:1200px;height:1200px;overflow:hidden;background:var(--stage)}
body{position:relative;font-family:"Open Sans",Arial,sans-serif;color:var(--ink)}
.spread{position:absolute;left:30px;width:1140px;height:500px;background:var(--paper);display:flex}
.spread--outside{top:60px}
.spread--inside{top:660px}
.spread-label{position:absolute;left:30px;top:630px;color:#bdbdbd;font-size:12px}
.panel{position:relative;width:380px;height:100%;border-right:1px solid var(--rule);overflow:hidden}
.panel:last-child{border-right:none}
.photo{position:absolute}
.serif{font-family:"Libre Baskerville",Georgia,serif}
.small{font-size:8.5px;line-height:1.5;color:var(--ink)}
.brand{position:absolute;display:flex;align-items:center;gap:6px;font-family:"Open Sans",Arial,sans-serif;font-size:9px;font-weight:600;color:var(--ink-soft);letter-spacing:.08em;text-transform:uppercase}
.brand-dot{width:14px;height:14px;border-radius:50%;background:var(--yellow)}

/* flap */
.flap-title{position:absolute;left:0;top:22px;background:var(--yellow);padding:8px 22px;font-size:15px;font-style:italic;color:#333}
.flap-sub{position:absolute;left:22px;top:68px;width:200px;font-size:9px;font-weight:600;border-bottom:1px solid var(--ink-soft);padding-bottom:3px}
.flap-photo{left:22px;top:92px;width:150px;height:130px;background:linear-gradient(160deg,var(--photo-warm),#b37a6a)}
.flap-quote{position:absolute;left:22px;top:236px;width:220px}
.tick-list{list-style:none;position:absolute;left:22px;width:220px}
.tick-list li{position:relative;padding-left:14px;font-size:8.5px;line-height:1.45;margin-bottom:5px;color:#b48f00;font-weight:600}
.tick-list li::before{content:"";position:absolute;left:0;top:3px;width:7px;height:7px;background:var(--yellow)}
.flap-foot{position:absolute;left:22px;bottom:18px;width:240px;font-size:8px;color:#b48f00;line-height:1.5}

/* back */
.back-photo{left:0;top:0;width:380px;height:150px;background:linear-gradient(120deg,var(--photo-cool),#e9dccd 60%,#f0c98e)}
.contact{position:absolute;left:22px;top:180px;width:340px}
.contact h3{font-size:11px;color:#333;margin-bottom:8px}
.contact-cols{display:flex;gap:18px}
.contact-cols p{font-size:8px;line-height:1.55}
.map{left:22px;top:300px;width:336px;height:120px;background:var(--map)}
.back-bar{position:absolute;left:0;bottom:0;width:100%;height:44px;background:var(--yellow)}

/* cover */
.cover-title{position:absolute;left:130px;top:70px}
.cover-title .haus{font-size:20px;letter-spacing:.15em;color:#555}
.cover-title .name{font-size:30px;color:#555;line-height:1.1}
.cover-title .tag{font-size:10px;font-style:italic;color:var(--ink-soft);margin-top:4px}
.cover-photo{left:0;top:160px;width:380px;height:180px;background:linear-gradient(180deg,#bcd3e6,#f4f4f0 45%,var(--photo-green))}
.cover-band{position:absolute;left:0;top:340px;width:380px;height:120px;background:var(--yellow);padding:22px 30px 0 130px}
.cover-band p{font-family:"Libre Baskerville",Georgia,serif;font-style:italic;font-size:17px;line-height:1.35;color:#333}
.cover-url{position:absolute;right:18px;bottom:12px;font-size:8px;color:var(--ink-soft)}

/* inside */
.statement-head{position:absolute;left:22px;top:16px;font-size:9px;font-style:italic;color:var(--ink-soft)}
.statement-quote{position:absolute;left:22px;top:42px;width:320px;border-left:3px solid var(--yellow);padding-left:12px;font-size:14px;line-height:1.35;font-style:italic;color:#c9a000}
.statement-sign{position:absolute;left:36px;top:196px;font-size:9px;font-style:italic}
.statement-body{position:absolute;left:22px;top:222px;width:330px}
.statement-body p{margin-bottom:6px}
.inside-foot{position:absolute;left:0;bottom:0;width:1140px;height:22px;background:var(--yellow-soft);display:flex;align-items:center;gap:70px;padding-left:22px;font-size:8px;font-weight:600;color:#6b5a00;z-index:2}
.caption{position:absolute;font-size:7.5px;line-height:1.45;color:var(--ink-soft)}
.bullet-mark{display:inline-block;width:6px;height:6px;background:var(--yellow);margin-right:5px}
</style>
</head>
<body>

<section class="spread spread--outside">
  <div class="panel panel--flap">
    <div class="flap-title serif">Von den Besten begleitet …</div>
    <div class="flap-sub">Heim- und Pflegedienstleitung</div>
    <div class="photo flap-photo" role="img" aria-label="Porträtfoto der Heimleiterin"></div>
    <p class="flap-quote small"><b>Mag. Klara Brunner-Weiss</b> leitet das Haus seit vielen Jahren. „Modernes Leben im Gesundheitsmanagement“ ist ihr Leitsatz, Master of Science für Gerontologie.</p>
    <ul class="tick-list" style="top:300px">
      <li>Seit 18 Jahren im Haus tätig</li>
      <li>Seit 12 Jahren Heim- und Pflegedienstleitung</li>
      <li>Seit über 15 Jahren erfahren als Heimleiterin und Gesundheitsmanagerin</li>
      <li>Seit Jahren zertifizierte Ausbildnerin für integrative Pflegekonzepte</li>
    </ul>
    <p class="flap-foot">Haben Sie Fragen? Gerne beantworten wir alle Anliegen persönlich.<br>Kontakt: Telefonnummer +43 (0)5 12/3 40 77</p>
  </div>

  <div class="panel panel--back">
    <div class="photo back-photo" role="img" aria-label="Foto einer Bewohnerin mit Pflegerin"></div>
    <div class="brand" style="left:22px;top:160px"><span class="brand-dot"></span>Lindenhof Verbund</div>
    <div class="contact">
      <h3>Kontakt:</h3>
      <div class="contact-cols">
        <p><b>Haus Lindenhof</b><br>Wiesengasse 12<br>4020 Talheim<br>Österreich</p>
        <p>Telefon<br>Fax<br>E-Mail<br>Web</p>
        <p>+43 (0)5 12/3 40 77<br>+43 (0)5 12/3 40 78<br>info@haus-lindenhof.at<br>www.haus-lindenhof.at</p>
      </div>
    </div>
    <div class="photo map" role="img" aria-label="Lageplan mit Anfahrt zum Haus"></div>
    <div class="back-bar"></div>
  </div>

  <div class="panel panel--cover">
    <div class="brand" style="right:18px;top:18px"><span class="brand-dot"></span>Lindenhof Verbund</div>
    <div class="cover-title serif">
      <div class="haus">HAUS</div>
      <div class="name">Lindenhof</div>
      <div class="tag">Ein Heim mit Stadtblick &amp; Wärme</div>
    </div>
    <div class="photo cover-photo" role="img" aria-label="Foto des Heimgebäudes im Grünen"></div>
    <div class="cover-band"><p>Führend in Seniorenbetreuung und Altenpflege</p></div>
    <div class="cover-url">www.haus-lindenhof.at</div>
  </div>
</section>

<div class="spread-label">Innenseite</div>

<section class="spread spread--inside">
  <div class="panel panel--statement">
    <div class="statement-head serif">Persönliches Statement der Leitung</div>
    <div class="statement-quote serif">„Das Lindenhof ist ein Haus der Begegnung, in welchem die Senioren motiviert werden, entsprechend ihrer Biografie, Bedürfnisse und Fähigkeiten, kompetent und selbstbestimmt ihr Leben zu gestalten.“</div>
    <div class="statement-sign serif">(Klara Brunner-Weiss)</div>
    <div class="statement-body small">
      <p>Unser Team begleitet jeden Menschen mit Respekt und Geduld. Wir achten auf Würde, Nähe und einen Alltag, der Freude schenkt und Sicherheit gibt.</p>
      <p>Durch jährliche Schulungen der Mitarbeiter sind wir Experten für:</p>
      <p><span class="bullet-mark"></span><b style="color:#b48f00">Spezielle Kommunikationstechniken</b><br><span class="bullet-mark"></span><b style="color:#b48f00">Qualitätssicherung und Sicherheit</b><br><span class="bullet-mark"></span><b style="color:#b48f00">Aromatherapie</b><br><span class="bullet-mark"></span><b style="color:#b48f00">Wundmanagement</b></p>
      <p>Durch jährliche Schulungen bleiben wir stets auf dem neuesten Stand und bieten eine Pflege, die Vertrauen schafft.</p>
    </div>
  </div>

  <div class="panel panel--gallery">
    <div class="photo" role="img" aria-label="Foto einer Bewohnerin im Gespräch" style="left:14px;top:14px;width:168px;height:150px;background:linear-gradient(150deg,#e7d6c2,#a8876f)"></div>
    <div class="photo" role="img" aria-label="Foto zweier Seniorinnen" style="left:190px;top:14px;width:176px;height:150px;background:linear-gradient(150deg,#d8b9a0,#8f6a58)"></div>
    <div class="photo" role="img" aria-label="Foto Pflegerin mit Bewohner im Rollstuhl" style="left:14px;top:172px;width:168px;height:140px;background:linear-gradient(160deg,var(--photo-cool),#7f98a8)"></div>
    <div class="photo" role="img" aria-label="Foto Bewohnerin beim Lesen" style="left:14px;top:320px;width:120px;height:130px;background:linear-gradient(160deg,#eee8e0,#b9a99a)"></div>
    <p class="caption" style="left:142px;top:330px;width:150px">Bild 1: Gemeinsame Stunden im Garten.<br>Bild 2: Aktivitäten am Nachmittag.<br>Bild 3: Therapie und Bewegung.<br>Bild 4: Ruhe im eigenen Zimmer.</p>
  </div>

  <div class="panel panel--care">
    <div class="photo" role="img" aria-label="Foto einer Pflegerin mit Seniorin" style="left:22px;top:16px;width:110px;height:120px;background:linear-gradient(160deg,#f3efe9,#c7b29f)"></div>
    <div class="small" style="position:absolute;left:142px;top:20px;width:220px">Wir sind für Sie da, rund um die Uhr und mit offenem Ohr. Ob Kurzzeitpflege oder dauerhaftes Wohnen, wir finden gemeinsam den passenden Weg.</div>
    <div class="small" style="position:absolute;left:22px;top:148px;width:340px">Jeder Tag im Haus bietet Raum für Begegnung, Bewegung und Ruhe. Unsere Angebote reichen von Gedächtnistraining über Musik bis zu kleinen Ausflügen in die Umgebung. Angehörige sind herzlich willkommen und werden in die Betreuung eingebunden. Gemeinsam gestalten wir Feste im Jahreskreis, pflegen Traditionen und schaffen ein Zuhause, in dem man sich geborgen fühlt. Unsere Küche kocht täglich frisch und regional, auf Wunsch auch Diätkost. Speziell geschulte Fachkräfte begleiten Menschen mit Demenz mit viel Einfühlungsvermögen und klarer Tagesstruktur.</div>
    <div class="photo" role="img" aria-label="Foto zweier Hände, die sich halten" style="left:22px;top:330px;width:340px;height:120px;background:linear-gradient(120deg,#e9d7c4,#c59a7f)"></div>
  </div>

  <div class="inside-foot"><span>HAUS Lindenhof</span><span>Ein Heim mit Stadtblick &amp; Wärme</span><span>Kontakt: Telefonnummer +43 (0)5 12/3 40 77</span><span>www.haus-lindenhof.at</span></div>
</section>

</body>
</html>
```